Flyer Design

I need a flyer as Iam starting a business which cleans Leather couches,sofas,chairs for residential and businesses.
We clean the interiors of automobiles and marine craft, boats large and small.
We would like to be able to get across the message that we are affordable, personal and reliable.
The Gold coast is our market and within this area there is a large amount of holiday apartments and houses which do experience high traffic to their living and dinning areas.

Target Market(s)

Target market Home,Apartment,Marine and Auto Owners

Industry/Entity Type

Residential

Requirements
Must have
• The flyer must have Company name which is BRIGHT HIDE CARE MOBILE NUMBER
0471932054
EMAIL marvtolk@quellnet.com
Colours would like bright Gold or green or Red eith black lettering very modern font
Nice to have
• I would like to keep it as simple and clean looking.but eye catching
Should not have
• Dont want the flyer to look like a Real Estate flyer or a pizza advertisement.

```html
<!DOCTYPE html>
<html lang="en">
<head>
<meta charset="utf-8">
<title>Bright Hide Care – Flyer</title>
<link href="https://fonts.googleapis.com/css2?family=Didact+Gothic&family=Montserrat:wght@700&display=swap" rel="stylesheet">
<style>
  :root {
    --page: #e4e4e4;
    --khaki: #857146;
    --corner: #3b3835;
    --rust: #8a3f1c;
    --gold: #c68b1f;
    --orange: #c2561a;
    --taupe: #9a8c70;
    --dark: #35302b;
    --ink: #111;
    --white: #fff;
    --cream: #d9c7a1;
  }
  * { margin: 0; padding: 0; box-sizing: border-box; }
  html, body { width: 1200px; height: 1000px; overflow: hidden; }
  body { background: var(--page); font-family: "Didact Gothic", sans-serif; }

  .flyer {
    position: absolute; left: 100px; top: 160px;
    width: 1000px; height: 680px; overflow: hidden;
    box-shadow: 0 18px 40px rgba(0,0,0,.35);
  }
  .flyer-bands { position: absolute; inset: 0; }

  .company-name {
    position: absolute; left: 0; top: 200px; width: 1000px;
    text-align: center;
    font-family: "Montserrat", sans-serif; font-weight: 700;
    font-size: 60px; line-height: 1; letter-spacing: 1px;
    color: var(--white); text-transform: uppercase; white-space: nowrap;
  }

  .tagline {
    position: absolute; left: 36px; top: 340px;
    font-family: "Montserrat", sans-serif; font-weight: 700;
    font-size: 44px; color: var(--ink); letter-spacing: .5px; white-space: nowrap;
  }
  .services {
    position: absolute; left: 40px; top: 408px; width: 360px;
    font-size: 13px; line-height: 1.45; color: var(--white);
  }
  .contact {
    position: absolute; left: 330px; top: 510px;
    color: var(--cream); font-family: "Didact Gothic", sans-serif; font-size: 30px;
    list-style: none;
  }
  .contact__item { display: flex; align-items: center; gap: 14px; margin-bottom: 14px; }
  .contact__icon { width: 30px; height: 30px; flex: none; }
</style>
</head>
<body>
  <main class="flyer">
    <svg class="flyer-bands" viewBox="0 0 1000 680" width="1000" height="680" role="img" aria-label="Diagonal bands of leather in rust, khaki, gold, taupe and dark brown">
      <defs>
        <linearGradient id="strap-tone" x1="0" y1="0" x2="1" y2="0">
          <stop offset="0" stop-color="var(--gold)"/>
          <stop offset=".7" stop-color="var(--gold)"/>
          <stop offset="1" stop-color="var(--orange)"/>
        </linearGradient>
      </defs>
      <rect width="1000" height="680" fill="var(--khaki)"/>
      <polygon points="0,40 150,0 700,0 0,230" fill="var(--rust)"/>
      <polygon points="0,0 150,0 0,40" fill="var(--corner)"/>
      <polygon points="0,240 1000,490 1000,570 0,370" fill="var(--taupe)"/>
      <polygon points="0,370 1000,570 1000,680 0,680" fill="var(--dark)"/>
      <polygon points="0,190 1000,440 1000,490 0,240" fill="url(#strap-tone)"/>
    </svg>

    <h1 class="company-name">Bright Hide Care</h1>

    <p class="tagline">Affordable....Personal....Reliable.</p>

    <p class="services">We clean Leather couches,sofas,chairs for residential and businesses. Also We clean the interiors of automobiles and marine craft, boats large and small.</p>

    <ul class="contact">
      <li class="contact__item">
        <svg class="contact__icon" viewBox="0 0 30 30" aria-hidden="true">
          <circle cx="15" cy="15" r="13" fill="none" stroke="var(--cream)" stroke-width="2"/>
          <path d="M11 8 l3 0 l1 4 l-2 1.5 q1.5 3 4 4.5 l1.5 -2 l4 1 l0 3 q-8 1 -11.5 -12 z" fill="var(--cream)"/>
        </svg>
        <span>0471932054</span>
      </li>
      <li class="contact__item">
        <svg class="contact__icon" viewBox="0 0 30 30" aria-hidden="true">
          <rect x="2" y="7" width="26" height="17" fill="var(--cream)"/>
          <path d="M2 7 L15 17 L28 7" fill="none" stroke="var(--dark)" stroke-width="2"/>
        </svg>
        <span>marvtolk@quellnet.com</span>
      </li>
    </ul>
  </main>
</body>
</html>
```